KAV cards & more
Business cards, fax cover sheet, letterhead, envelopes, powerpoint slide template
Modern
Tad Willers
Owner
17 Lindgate Row Alderwick, NJ 08044
twkav@mailvane.net
Please integrate my already-completed company logo (attached) in a clean, modern design for business cards, Fax cover sheet, letterhead, envelopes, and powerpoint slide template

```html
<!DOCTYPE html>
<html lang="en">
<head>
<meta charset="utf-8">
<title>KAV Business Card</title>
<link rel="stylesheet" href="https://fonts.googleapis.com/css2?family=Open+Sans:wght@400;600;700&display=swap">
<style>
  :root {
    --stage: #e6e8e6;
    --card-white: #ffffff;
    --green: #3f9e2c;
    --green-light: #6cc13a;
    --green-dark: #1f7f33;
    --text-grey: #8a8f8a;
    --watermark: #eef0ee;
    --watermark-on-green: rgba(255,255,255,0.28);
  }
  * { box-sizing: border-box; margin: 0; padding: 0; }
  html, body {
    width: 1200px; height: 871px; overflow: hidden;
    background: var(--stage);
    font-family: "Open Sans", Arial, sans-serif;
  }
  .sheet {
    position: relative; width: 1200px; height: 871px;
    display: flex; align-items: center; justify-content: center; gap: 60px;
  }
  .card {
    position: relative; width: 500px; height: 286px;
    border-radius: 22px; overflow: hidden;
    box-shadow: 0 10px 28px rgba(0,0,0,0.18);
  }
  .card-front { background: var(--card-white); }
  .card-back {
    background: radial-gradient(circle at 35% 25%, var(--green-light), var(--green) 45%, var(--green-dark) 100%);
  }
  .watermark { position: absolute; border-radius: 50%; }
  .card-front .watermark {
    width: 104px; height: 104px; right: 90px; top: 10px;
    background: var(--watermark);
  }
  .card-back .watermark {
    width: 110px; height: 110px; left: 50%; top: 50%;
    transform: translate(-50%, -50%);
    background: var(--watermark-on-green);
  }
  .brand {
    position: absolute; left: 34px; top: 118px;
    display: flex; align-items: center; gap: 10px;
  }
  .brand-dot { width: 30px; height: 30px; border-radius: 50%; background: var(--green); }
  .brand-name {
    font-weight: 700; font-size: 34px; letter-spacing: 2px; color: var(--green);
    line-height: 1;
  }
  .brand-rule {
    position: absolute; left: 34px; top: 160px; width: 148px; height: 1px;
    background: var(--green);
  }
  .person { position: absolute; left: 230px; top: 128px; }
  .person-name { font-weight: 700; font-size: 15px; color: var(--green); }
  .person-title { font-size: 11px; color: var(--text-grey); margin-top: 2px; }
  .contact {
    position: absolute; left: 34px; bottom: 24px;
    font-size: 8.5px; line-height: 1.45; color: var(--text-grey);
    list-style: none;
  }
</style>
</head>
<body>
  <main class="sheet">
    <section class="card card-front" aria-label="Business card front">
      <div class="watermark" aria-hidden="true"></div>
      <div class="brand">
        <span class="brand-dot" aria-hidden="true"></span>
        <span class="brand-name">KAV</span>
      </div>
      <div class="brand-rule" aria-hidden="true"></div>
      <div class="person">
        <p class="person-name">Tad Willers</p>
        <p class="person-title">Owner</p>
      </div>
      <ul class="contact">
        <li>17 Lindgate Row</li>
        <li>Alderwick, NJ 08044</li>
        <li>p: 555.010.2284</li>
        <li>f: 555.010.2285</li>
        <li>twkav@mailvane.net</li>
      </ul>
    </section>
    <section class="card card-back" aria-label="Business card back">
      <div class="watermark" aria-hidden="true"></div>
    </section>
  </main>
</body>
</html>
```